Clean Brochure Design

Hello,

I need a brochure made that is a folded in half 17" x 11"

The design needs to fit the website and please grab some content off the site for the mockup.

Need it to be clean and professional but with some style, similar to the website.

http://linkbrevo.net/qmrpxwa

Please let me know if you have any questions.

```html
<!DOCTYPE html>
<html lang="en">
<head>
<meta charset="utf-8">
<title>Meridian HR – Presentation Folder</title>
<link href="https://fonts.googleapis.com/css2?family=Open+Sans:wght@300;400;700&family=Tinos:wght@400;700&display=swap" rel="stylesheet">
<style>
  :root {
    --page-bg: #e4e4e4;
    --paper: #ffffff;
    --paper-shade: #eeeeee;
    --brand-blue: #1f5fb0;
    --brand-blue-deep: #1b3f9a;
    --brand-navy: #0f2a52;
    --accent-cyan: #5fc6e8;
    --ink: #333a44;
    --photo-light: #d4d6d8;
    --photo-dark: #8d9194;
  }
  * { margin: 0; padding: 0; box-sizing: border-box; }
  html, body { width: 1200px; height: 847px; overflow: hidden; background: var(--page-bg); }

  .spread {
    position: absolute; left: 50px; top: 67px;
    width: 1100px; height: 712px;
    display: flex;
    box-shadow: 0 6px 24px rgba(0,0,0,.18);
  }
  .panel { position: relative; width: 550px; height: 712px; overflow: hidden; }
  .panel--back { background: linear-gradient(160deg, var(--paper) 0%, var(--paper-shade) 100%); }
  .panel--front { background: var(--paper); }
  .panel svg.band { position: absolute; left: 0; top: 0; width: 550px; height: 712px; }

  .brand {
    position: absolute;
    font-family: "Open Sans", sans-serif;
    font-weight: 700;
    color: var(--brand-navy);
    line-height: 1;
  }
  .brand__name { font-size: 26px; letter-spacing: -0.5px; }
  .brand__tagline {
    display: block; margin-top: 3px;
    font-size: 7px; font-weight: 400; letter-spacing: 1px; text-transform: uppercase;
    color: var(--brand-navy);
  }
  .brand--back { left: 62px; top: 405px; }
  .brand--front { right: 62px; top: 48px; text-align: right; }

  .office {
    position: absolute; left: 62px; top: 450px;
    font-family: "Tinos", serif; font-size: 10px; line-height: 1.45; color: var(--ink);
  }
  .office__title { font-weight: 700; font-style: italic; margin-bottom: 6px; }
  .office__lines { margin-bottom: 6px; }

  .call {
    position: absolute; left: 62px; top: 624px;
    font-family: "Open Sans", sans-serif; font-weight: 300; font-size: 24px;
    color: var(--paper); letter-spacing: .5px;
  }
  .call__label { color: var(--accent-cyan); }

  .intro {
    position: absolute; left: 248px; top: 186px; width: 250px;
    font-family: "Open Sans", sans-serif; font-weight: 700; font-size: 8.5px; line-height: 1.35;
    color: var(--brand-blue);
  }
  .intro-rule { position: absolute; left: 248px; top: 230px; width: 302px; height: 7px; background: var(--brand-blue-deep); }

  .photo {
    position: absolute; left: 30px; top: 240px; width: 520px; height: 236px;
    background: linear-gradient(120deg, var(--photo-light) 0%, #b7babd 45%, var(--photo-dark) 100%);
  }

  .tagline {
    position: absolute; right: 30px; top: 582px;
    font-family: "Tinos", serif; font-size: 17px; color: var(--paper);
  }
</style>
</head>
<body>
  <main class="spread">
    <section class="panel panel--back" aria-label="Back cover">
      <svg class="band" viewBox="0 0 550 712" aria-hidden="true">
        <rect x="0" y="568" width="550" height="144" fill="var(--brand-blue)"/>
        <path d="M70 612 Q200 560 380 568" fill="none" stroke="#ffffff" stroke-width="3" stroke-linecap="round"/>
        <path d="M90 618 Q210 574 360 576" fill="none" stroke="#ffffff" stroke-width="1.2" stroke-linecap="round" opacity=".7"/>
      </svg>
      <div class="brand brand--back">
        <span class="brand__name">Meridian HR</span>
        <span class="brand__tagline">Your Partner in Workforce Growth</span>
      </div>
      <address class="office">
        <div class="office__title">Arizona Office</div>
        <div class="office__lines">1200 Harbor View Drive<br>Suite 210<br>Fairview, AZ 85000</div>
        <div>Phone: (555) 014 2290<br>Fax: (555) 014 2291</div>
      </address>
      <div class="call"><span class="call__label">Call</span> 1.800.555.0172</div>
    </section>

    <section class="panel panel--front" aria-label="Front cover">
      <div class="brand brand--front">
        <span class="brand__name">Meridian HR</span>
        <span class="brand__tagline">Your Partner in Workforce Growth</span>
      </div>
      <p class="intro">Meridian HR helps growing teams build a safer and more compliant workplace, reducing costs so owners can focus on work.</p>
      <div class="intro-rule"></div>
      <div class="photo" role="img" aria-label="Black and white photo of a manager and a worker in a hard hat reviewing a document in a warehouse"></div>
      <svg class="band" viewBox="0 0 550 712" aria-hidden="true">
        <rect x="300" y="476" width="250" height="9" fill="var(--brand-blue-deep)"/>
        <path d="M0 530 C150 540 300 540 420 520 C480 510 520 505 550 506 L550 712 L0 712 Z" fill="var(--brand-blue)"/>
        <path d="M0 530 C120 536 200 538 260 537 L260 712 L0 712 Z" fill="var(--brand-blue-deep)" opacity=".6"/>
        <path d="M270 575 Q380 530 520 528" fill="none" stroke="#ffffff" stroke-width="3" stroke-linecap="round"/>
        <path d="M290 580 Q390 544 500 540" fill="none" stroke="#ffffff" stroke-width="1.2" stroke-linecap="round" opacity=".7"/>
      </svg>
      <div class="tagline">Empowering Business Success</div>
    </section>
  </main>
</body>
</html>
```